Website for a Party Bus charter business

Please prepare a site for a local party bus charter company names Holloway Bus Company.
They hire a party bus, chatrer bus, boat hire and party trailer hire (place holder photos fine for these items).
I have included a wireframe design. This should be used, however creative licence is fully extended
Delivery of PSD is required and all fonts and source files
The client likes: http://www.tallquorin.com.au/ but must not look completely the same.
Should use a gold (simualr to #D1CFA1) colour, even if just background.
Updates
Hi All, just wondering if anyone is working on this as I have not received any responses or questions?
Is there anything I can do to assist?
Thanks all for the great submissions. I will be sending these onto the client today. Will let you know the outcome as soon as I can
Industry/Entity Type
Business
Look and feel
Each slider illustrates characteristics of the customer's brand and the style your logo design should communicate.

```html
<!DOCTYPE html>
<html lang="en">
<head>
<meta charset="utf-8">
<title>Holloway Bus Company</title>
<link rel="stylesheet" href="https://fonts.googleapis.com/css2?family=Lilita+One&family=Open+Sans:wght@400;600;700&display=swap">
<style>
  :root {
    --gold: #d3cf9f;
    --brown: #8e7650;
    --caption-brown: #9a8055;
    --navy: #1d4f7a;
    --peach: #fce5cb;
    --grey: #f2f2f2;
    --tab-blue: #33bcdc;
    --tab-green: #8fc84a;
    --tab-red: #f0436a;
    --text: #444;
    --footer-text: #6b6a50;
    --white: #fff;
  }
  * { box-sizing: border-box; margin: 0; padding: 0; }
  html, body { width: 1200px; height: 900px; overflow: hidden; }
  body { position: relative; background: var(--white); font-family: "Open Sans", Arial, sans-serif; color: var(--text); }
  .abs { position: absolute; }

  .site-header { left: 0; top: 0; width: 1200px; height: 44px; background: var(--gold); }
  .brand { left: 160px; top: 0; height: 44px; line-height: 44px; font-family: "Open Sans", sans-serif;
    font-weight: 700; font-size: 22px; letter-spacing: 1px; color: var(--brown); }
  .main-nav { right: 200px; top: 0; height: 44px; display: flex; align-items: center; }
  .main-nav a { font-weight: 700; font-size: 13px; letter-spacing: 1.3px; color: #4c4a3a; text-decoration: none; padding: 0 21px; border-left: 1px solid #8b896a; line-height: 14px; }
  .main-nav a:first-child { border-left: none; }
  .main-nav a:last-child { padding-right: 0; }

  .hero { left: 0; top: 44px; width: 1200px; height: 288px;
    background: linear-gradient(100deg, #1a1b2a 0%, #3a3550 18%, #e9e9ec 30%, #dcdce2 60%, #6a4ed8 80%, #2a3aa0 100%); }
  .hero-caption { left: 220px; top: 165px; width: 780px; height: 51px; background: rgba(70,52,20,.85);
    color: var(--white); font-family: "Lilita One", sans-serif; font-size: 32px; letter-spacing: 4.5px; line-height: 51px; padding-left: 156px; white-space: nowrap; }

  .feature-photo { height: 84px; }
  .feature-title { font-weight: 700; font-size: 14px; line-height: 12px; letter-spacing: 1.2px; color: var(--caption-brown); text-transform: uppercase; white-space: nowrap; }

  .highlight { left: 0; top: 512px; width: 1200px; height: 160px; background: var(--peach); }
  .highlight-title { left: 485px; top: 535px; width: 536px; font-weight: 700; font-size: 16px; line-height: 15px; letter-spacing: 1.5px; color: var(--navy); text-transform: uppercase; }
  .highlight-title .justify { display: block; text-align: justify; text-align-last: justify; }
  .highlight-text { left: 487px; top: 582px; width: 540px; font-size: 12px; line-height: 13px; letter-spacing: .4px; color: #333; }
  .read-more { left: 485px; top: 632px; font-size: 10px; letter-spacing: .5px; color: #333; }

  .lower { left: 0; top: 672px; width: 1200px; height: 173px; background: var(--grey); }
  .tab { top: 689px; height: 24px; color: var(--white); font-weight: 700; font-size: 12px; line-height: 24px; padding-left: 30px; }
  .tab-blue { left: 150px; width: 167px; background: var(--tab-blue); }
  .tab-green { left: 317px; width: 145px; background: var(--tab-green); padding-left: 21px; }
  .tab-red { left: 462px; width: 137px; background: var(--tab-red); padding-left: 18px; }
  .tab-panel { left: 150px; top: 713px; width: 525px; height: 110px; background: var(--tab-blue); }
  .tab-title { left: 374px; top: 733px; color: var(--white); font-weight: 700; font-size: 11px; }
  .tab-text { left: 374px; top: 754px; width: 268px; color: var(--white); font-size: 7px; line-height: 10px; }
  .tab-more { left: 563px; top: 796px; color: var(--white); font-weight: 700; font-size: 8px; display: flex; align-items: center; gap: 4px; }
  .side-caption { left: 708px; top: 780px; width: 320px; font-size: 14px; line-height: 15px; color: var(--caption-brown); letter-spacing: .5px; }

  .site-footer { left: 0; top: 845px; width: 1200px; height: 55px; background: var(--gold); }
  .footer-nav { left: 152px; top: 865px; display: flex; gap: 31px; }
  .footer-nav a, .copyright { font-size: 9.5px; color: var(--footer-text); text-decoration: none; }
  .copyright { right: 190px; top: 865px; font-size: 10px; }
</style>
</head>
<body>
  <header class="site-header abs"></header>
  <div class="brand abs">HOLLOWAY BUS</div>
  <nav class="main-nav abs">
    <a href="#">HOME</a><a href="#">ABOUT</a><a href="#">SERVICES</a><a href="#">PRICING</a><a href="#">CONTACT</a>
  </nav>

  <div class="hero abs" role="img" aria-label="White double-decker party bus parked at night in front of a purple-lit building"></div>
  <div class="hero-caption abs">LOREM IPSUM DOLOR SIT</div>

  <div class="feature-photo abs" style="left:152px;top:364px;width:422px;background:linear-gradient(90deg,#6a4a3a,#2a2a2e 40%,#3a3a3e 80%,#8a8a88);" role="img" aria-label="Black limousine party bus with red livery"></div>
  <div class="feature-photo abs" style="left:596px;top:364px;width:421px;background:linear-gradient(90deg,#1a2a6a,#2a5ab0 40%,#1a3a7a 70%,#2a2a5a);" role="img" aria-label="Party bus interior with blue and green club lighting"></div>
  <div class="feature-title abs" style="left:150px;top:458px;">Lorem Ipsum has been the industry's<br>standard dummy</div>
  <div class="feature-title abs" style="left:597px;top:458px;">Lorem Ipsum has been the industry's<br>standard dummy</div>

  <section class="highlight abs"></section>
  <div class="abs" style="left:151px;top:541px;width:310px;height:102px;background:linear-gradient(180deg,#a8c8e8 0%,#e8eef4 45%,#6a8ab0 70%,#8a8a88 100%);" role="img" aria-label="Blue and white double-deck coach on a road"></div>
  <h2 class="highlight-title abs"><span class="justify">Lorem Ipsum has been the industry's</span>standard dummy text ever</h2>
  <p class="highlight-text abs">Lorem Ipsum has been the industry's standard dummy text ever since<br>the 1500s,</p>
  <a class="read-more abs">READ MORE [ + ]</a>

  <section class="lower abs"></section>
  <div class="tab tab-blue abs">Heading</div>
  <div class="tab tab-green abs">Heading</div>
  <div class="tab tab-red abs">Heading</div>
  <div class="tab-panel abs"></div>
  <div class="abs" style="left:176px;top:727px;width:164px;height:81px;background:linear-gradient(135deg,#5a3020,#a86a3a 50%,#3a2018);" role="img" aria-label="Guests enjoying a party inside a bus"></div>
  <h3 class="tab-title abs">Lertyakure setyebo doloes</h3>
  <p class="tab-text abs">Neryase nti masertas lertyakuhsety kertya aseticerertas faeskes kertyu erxvitae ertynemo lasepts goer. Navolemas auodit onsequuntur magni dolores eoqui rationevolupta tebenqui dolorem ipsumquia dolor.</p>
  <div class="tab-more abs">read more
    <svg width="7" height="7" viewBox="0 0 8 8"><circle cx="4" cy="4" r="4" fill="#fff"/><path d="M3 2l2 2-2 2" stroke="#33bcdc" stroke-width="1.2" fill="none"/></svg>
  </div>

  <div class="abs" style="left:707px;top:689px;width:311px;height:84px;background:linear-gradient(90deg,#3a2a20,#c8a888 40%,#e8d8c8 70%,#5a4a40);" role="img" aria-label="Group of young friends posing for a photo at a party"></div>
  <p class="side-caption abs">Lorem Ipsum has been the indus-<br>try's standard dummy text ever</p>

  <footer class="site-footer abs"></footer>
  <nav class="footer-nav abs"><a href="#">Home</a><a href="#">About</a><a href="#">Services</a><a href="#">Pricing</a><a href="#">Contact</a></nav>
  <p class="copyright abs">Desing © 2014. All right reserved. \ Privacy policy</p>
</body>
</html>
```